Halloway Crest Backers Guild business cards

Create a single-sided business card for the Halloway Crest Backers Guild based on the attached logo.
The additional data fields include Name, Title, Email, Phone, and website.
Please use the following as sample data:
Name: Dean Varrow
Title: Co-Founder / Investor
Email: deanvarrow@mailtern.net
Phone: 555-314-2706
Website: www.hcbackersguild.com

Target Market(s)

Start ups, entrepreneurs, venture capitalists

Industry/Entity Type

Investment

Contact Information for Business Card

Professional business card. Technology company.

Font styles to use
Serif
Sans Serif

Requirements
Must have
• Include the HCBG logo (attached)
• Name
• Title
• Email
• Phone
• Website
Should not have
• Cute, cartoony

```html
<!DOCTYPE html>
<html lang="en">
<head>
<meta charset="UTF-8">
<title>Halloway Crest Backers Guild – Business Card</title>
<link rel="stylesheet" href="https://fonts.googleapis.com/css2?family=Open+Sans:wght@400;600&display=swap">
<style>
  :root {
    --ground: #2e2e2e;
    --card-dark: #232323;
    --card-white: #ffffff;
    --band-dark: #2a2a2a;
    --band-grey: #dedede;
    --green: #0f9d48;
    --ink: #1c1c1c;
    --ink-soft: #333333;
    --logo-grey: #9a9a9a;
  }
  * { margin: 0; padding: 0; box-sizing: border-box; }
  html, body { width: 1200px; height: 800px; overflow: hidden; }
  body {
    background: var(--ground);
    font-family: "Open Sans", Arial, sans-serif;
    position: relative;
  }
  .card {
    position: absolute;
    top: 95px;
    width: 350px;
    height: 610px;
    overflow: hidden;
  }
  /* Back side */
  .card--back { left: 200px; background: var(--card-dark); }
  .card--back .accent-line {
    position: absolute;
    height: 1.5px;
    background: var(--green);
  }
  .card--back .accent-line--top { top: 48px; right: 0; width: 150px; }
  .card--back .accent-line--bottom { bottom: 48px; left: 0; width: 170px; }
  .brand {
    display: flex;
    align-items: center;
    gap: 10px;
  }
  .brand__mark {
    width: 16px; height: 16px;
    background: var(--green);
    flex: none;
  }
  .brand__name {
    font-weight: 600;
    font-size: 17px;
    line-height: 1.2;
    letter-spacing: 0.3px;
  }
  .card--back .brand {
    position: absolute;
    top: 50%; left: 50%;
    transform: translate(-50%, -50%);
    width: 240px;
  }
  .card--back .brand__name { color: var(--logo-grey); }

  /* Front side */
  .card--front { left: 650px; background: var(--card-white); }
  .card--front .edge-bands { position: absolute; inset: 0; }
  .card--front .brand {
    position: absolute;
    top: 70px; left: 120px;
    width: 200px;
  }
  .card--front .brand__name { color: var(--ink); }
  .person {
    position: absolute;
    top: 318px; left: 58px; right: 0;
  }
  .person__name {
    font-size: 30px;
    font-weight: 600;
    color: var(--ink);
    letter-spacing: -0.3px;
    line-height: 1.1;
  }
  .person__title-row {
    display: flex;
    align-items: center;
    gap: 4px;
    margin-top: 4px;
  }
  .person__title {
    font-size: 16px;
    color: var(--green);
    white-space: nowrap;
  }
  .person__rule {
    flex: 1;
    height: 2px;
    background: var(--green);
    margin-top: 14px;
  }
  .contact {
    list-style: none;
    margin-top: 2px;
  }
  .contact__item {
    display: flex;
    align-items: center;
    gap: 10px;
    font-size: 15px;
    color: var(--ink-soft);
    line-height: 30px;
  }
  .contact__icon { width: 15px; height: 15px; flex: none; }
</style>
</head>
<body>

<section class="card card--back" aria-label="Business card back">
  <span class="accent-line accent-line--top"></span>
  <div class="brand">
    <span class="brand__mark"></span>
    <span class="brand__name">Halloway Crest Backers Guild</span>
  </div>
  <span class="accent-line accent-line--bottom"></span>
</section>

<section class="card card--front" aria-label="Business card front">
  <svg class="edge-bands" viewBox="0 0 350 610" preserveAspectRatio="none" aria-hidden="true">
    <polygon points="0,0 28,0 28,330 0,380" fill="var(--band-dark)"/>
    <polygon points="0,380 28,330 50,330 50,560 0,600" fill="var(--band-grey)"/>
    <polygon points="0,510 50,510 50,560 0,610" fill="var(--green)"/>
  </svg>

  <div class="brand">
    <span class="brand__mark"></span>
    <span class="brand__name">Halloway Crest Backers Guild</span>
  </div>

  <div class="person">
    <h1 class="person__name">Dean Varrow</h1>
    <div class="person__title-row">
      <span class="person__title">Co-Founder / Investor</span>
      <span class="person__rule"></span>
    </div>
    <ul class="contact">
      <li class="contact__item">
        <svg class="contact__icon" viewBox="0 0 16 16" aria-hidden="true"><rect x="1" y="3" width="14" height="10" fill="var(--green)"/><polyline points="1,3 8,9 15,3" fill="none" stroke="#fff" stroke-width="1.3"/></svg>
        deanvarrow@mailtern.net
      </li>
      <li class="contact__item">
        <svg class="contact__icon" viewBox="0 0 16 16" aria-hidden="true"><path d="M1 6 Q8 0 15 6 L13 8 L11 6 L5 6 L3 8 Z" fill="var(--green)"/><rect x="3" y="8" width="10" height="6" rx="1" fill="var(--green)"/></svg>
        555-314-2706
      </li>
      <li class="contact__item">
        <svg class="contact__icon" viewBox="0 0 16 16" aria-hidden="true" fill="none" stroke="var(--green)" stroke-width="1.2"><circle cx="8" cy="8" r="6.5"/><ellipse cx="8" cy="8" rx="3" ry="6.5"/><line x1="1.5" y1="8" x2="14.5" y2="8"/></svg>
        www.hcbackersguild.com
      </li>
    </ul>
  </div>
</section>

</body>
</html>
```